Cloud Software Services Business Needs New Website Design

Our client is looking for a really modern design for their cloud services company. We have a logo, but apart from that, if you read the brief fully and digest the wireframes, we hope you will come up with a really amazing end product.

The design of the website should be professional and trustworthy, it is there to inspire confidence in the services and softwares, as well as emphasising the track record of VRN and relative knowledge and competencies.

Given all the cloud-related communications in the messaging on the site, we will need this in either the imagery or icons in the site so that we can connect the messaging with the service offering.

The brand, being black, gives full range for the designer to present a palette that serves the brand, not forgetting the audience are generally IT decision-makers.

Target Market(s)

Managers and Directors Responsible for IT/Cloud Infrastructure

Industry/Entity Type

IT Technology

Number of Pages Required

5+ page

Font styles to use
Sans Serif

Requirements
Must have
• Initial designs which match the brief and wireframes, focus on the homepage and the winning designer will need to supply the internal pages for the website.
Nice to have
• Clearly considered professional website designs, with consistent design work and branding. If choosing stock imagery, then from PixHarbor Basics please.
Should not have
• Not too much colour, or too consumer/youthful.

```html
<!DOCTYPE html>
<html lang="en">
<head>
<meta charset="utf-8">
<title>VRN – Cloud Services</title>
<link href="https://fonts.googleapis.com/css2?family=Montserrat:wght@400;500;600;700;800&display=swap" rel="stylesheet">
<style>
:root{
  --navy:#0c1459;
  --navy-deep:#151c86;
  --red:#e8332b;
  --ink:#2b2b33;
  --muted:#4a4a55;
  --pale-blue:#e2e8fb;
  --grey:#d9dadd;
  --white:#ffffff;
  --black:#000000;
}
*{box-sizing:border-box;margin:0;padding:0}
html,body{width:1200px;height:5078px;overflow:hidden}
body{font-family:'Montserrat',sans-serif;color:var(--ink);background:var(--white);position:relative}
.wrap{width:1026px;margin-left:87px;position:relative}
section,header{position:relative}
.btn{display:inline-flex;align-items:center;justify-content:center;font-weight:700;font-size:14px;text-transform:uppercase;letter-spacing:.2px}
.btn-white{background:var(--white);color:var(--navy)}
.btn-red{background:var(--red);color:var(--white);box-shadow:0 3px 6px rgba(0,0,0,.2)}
.btn-navy{background:var(--navy);color:var(--white)}
h2{color:var(--navy);font-weight:800;text-transform:uppercase;letter-spacing:.3px}

.topbar{height:48px;background:linear-gradient(90deg,#1a1f8e,#0c1459)}
.topbar ul{list-style:none;display:flex;justify-content:flex-end;gap:0;padding-right:87px;height:48px;align-items:center;font-size:11px;font-weight:700;color:var(--white)}
.topbar li+li::before{content:"|";margin:0 18px}

.nav{height:98px;display:flex;align-items:center;justify-content:space-between;padding:0 87px}
.brand{display:flex;align-items:center;gap:10px;font-size:40px;font-weight:700;color:var(--black);letter-spacing:1px}
.brand i{width:14px;height:14px;background:var(--black);border-radius:50%}
.nav ul{list-style:none;display:flex;gap:58px;font-size:16px;font-weight:700;color:var(--black)}

.hero{height:630px;margin:0 4px;background:linear-gradient(120deg,#0b1a8a 0%,#1238b8 45%,#0a8fd6 80%,#12b9e6 100%);overflow:hidden}
.hero-art{position:absolute;inset:0;background:radial-gradient(ellipse at 75% 70%,rgba(60,200,255,.45),transparent 55%),radial-gradient(ellipse at 25% 30%,rgba(30,90,220,.5),transparent 60%)}
.hero h1{position:absolute;top:118px;width:100%;text-align:center;color:var(--white);font-size:50px;font-weight:800;letter-spacing:.5px}
.hero .sub{position:absolute;top:316px;width:100%;text-align:center;color:var(--white);font-size:37px;font-weight:800}
.hero .btn{position:absolute;top:506px;height:56px;width:245px}

.promise{height:584px;padding-top:82px}
.promise h2{font-size:33px;margin-bottom:44px}
.promise p{font-size:15.5px;line-height:25px;color:var(--muted);max-width:880px;margin-bottom:32px}
.promise ol{font-size:15.5px;line-height:19px;color:var(--muted);margin:-22px 0 8px 34px}
.promise .cta{display:flex;align-items:center;gap:68px;font-size:15.5px;color:var(--muted)}
.promise .cta .btn{width:158px;height:38px;font-size:11px}

.tools{height:538px;margin:0 4px;background:linear-gradient(180deg,#f3f3f4,#cfd0d3)}
.tools-art{position:absolute;right:0;top:0;width:520px;height:538px;background:radial-gradient(ellipse at 55% 45%,rgba(30,190,210,.35),transparent 60%)}
.tools h2{position:absolute;left:83px;top:138px;font-size:38px}
.tools p{position:absolute;left:83px;top:236px;font-size:17px;font-weight:500;color:var(--muted);letter-spacing:.4px}
.tools .btn{position:absolute;left:83px;top:334px;width:245px;height:56px}

.move{height:430px;padding-top:76px;text-align:center}
.move h2{font-size:31px;margin-bottom:52px}
.carousel{display:flex;align-items:center;justify-content:space-between}
.arrow{width:44px;height:96px}
.cards{display:flex;gap:60px}
.card{width:245px;height:242px;background:#f6f6f7;box-shadow:0 3px 8px rgba(0,0,0,.12);display:flex;flex-direction:column;align-items:center;justify-content:flex-end;padding-bottom:36px}
.card .name{font-size:24px;font-weight:600;color:var(--navy);margin-bottom:58px;display:flex;align-items:center;gap:8px}
.card .name i{width:22px;height:22px;background:var(--navy)}
.card .btn{width:118px;height:28px;font-size:11px;font-weight:500}

.advice{height:426px;padding:92px 0 0 191px}
.advice h2{font-size:31px;margin-bottom:42px}
.advice p{font-size:13.5px;line-height:22px;font-weight:600;color:var(--muted);max-width:780px;margin-bottom:22px}

.costs{height:454px;margin:0 4px;background:var(--pale-blue);padding-top:70px;text-align:center}
.costs h2{font-size:31px}
.badge{position:absolute;left:284px;top:156px;width:192px;height:192px;border-radius:50%;background:var(--red);box-shadow:0 4px 10px rgba(0,0,0,.2);color:var(--white);display:flex;flex-direction:column;align-items:center;justify-content:center}
.badge b{font-size:36px;font-weight:700;line-height:40px}
.badge span{font-size:19px;font-weight:600}
.costs .copy{position:absolute;left:518px;top:148px;width:450px;text-align:left;font-size:13.5px;line-height:22px;font-weight:600;color:var(--muted)}
.costs .copy p{margin-bottom:22px}
.costs .copy .btn{position:absolute;left:262px;top:240px;width:158px;height:36px;font-size:11px;font-weight:600;background:var(--white);color:var(--navy)}

.start{height:396px;padding-top:84px;text-align:center}
.start h2{font-size:31px;margin-bottom:46px}
.start p{font-size:13.5px;line-height:22px;font-weight:600;color:var(--muted);width:790px;margin:0 auto 52px}
.start .row{display:flex;justify-content:center;gap:190px}
.start .btn{width:245px;height:55px;font-size:15px}

.blog{height:494px;margin:0 4px;background:var(--pale-blue);padding-top:58px;text-align:center}
.blog h2{font-size:31px;margin-bottom:52px}
.posts{display:flex;gap:17px;margin-left:83px}
.post{width:244px}
.post .thumb{height:245px;background:linear-gradient(180deg,#bfe3f5,#a9d6ee)}
.post h3{font-size:15px;font-weight:600;color:var(--black);margin-top:24px}

.trusted{height:450px;padding-top:68px;text-align:center}
.trusted h2{font-size:31px;margin-bottom:80px}
.logos{display:flex;gap:17px;margin-left:87px}
.logo-box{width:244px;height:126px;background:var(--white);box-shadow:0 3px 8px rgba(0,0,0,.13);display:flex;align-items:center;justify-content:center;font-size:30px;font-weight:600;color:var(--navy)}
.logo-box .mark{width:70px;height:70px;background:var(--navy)}

.footer{height:522px;margin:0 4px;background:var(--black);color:var(--white);padding:118px 0 0 83px;display:flex}
.footer .col{width:261px}
.footer h4{font-size:19px;font-weight:800;text-transform:uppercase;margin-bottom:20px}
.footer ul{list-style:none;font-size:11px;line-height:31.5px}
.footer address{font-style:normal;font-size:11px;line-height:21px;margin-top:76px}
</style>
</head>
<body>
<header>
  <nav class="topbar"><ul><li>Partner</li><li>Blog</li><li>About Us</li><li>Contact Us</li></ul></nav>
  <div class="nav">
    <div class="brand"><i></i>VRN</div>
    <ul><li>Home</li><li>Cloud</li><li>Service</li><li>Software</li></ul>
  </div>
</header>

<section class="hero">
  <div class="hero-art" role="img" aria-label="Isometric illustration of server racks in a data centre with a person at a glowing console"></div>
  <h1>OPERATING UNDER A CLOUD</h1>
  <div class="sub">THERE’S A SILVER LINING</div>
  <a class="btn btn-white" style="left:83px">Reducing Costs</a>
  <a class="btn btn-white" style="left:460px">Migration</a>
  <a class="btn btn-white" style="left:866px">Work With Us</a>
</section>

<section class="promise"><div class="wrap">
  <h2>Did the promise of cloud computing happen for you</h2>
  <p>We Didn’t think so! You’re not alone. There are many companies just like you who believed in the promise of cloud computing but are now shackled it.</p>
  <p>But there is a silver lining . which is that VRN have built a business around helping companies improve their cloud efficiencies, reduce costs and simplify their operations as a result.</p>
  <p style="margin-top:54px">It can be summarised in three promises VRN makes to every client or partner:</p>
  <ol>
    <li>You can reduce cloud costs, without needing to move supplier</li>
    <li>You can &nbsp;migrate from one cloud to another more easily</li>
    <li>You can simplify your cloud management and choose your favoured provider</li>
  </ol>
  <div class="cta"><span>If you already know or want to talk to us just call 01632 960 418 or</span><a class="btn btn-red">Send an Email</a></div>
</div></section>

<section class="tools">
  <div class="tools-art" role="img" aria-label="Isometric illustration of teal cloud servers connected by circuit lines with security icons"></div>
  <h2>Your Cloud, Your Tools</h2>
  <p>A SUITE OF SOFTWARE TO SIMPLIFY DEPLOYMENT</p>
  <a class="btn btn-white">Cloud Software</a>
</section>

<section class="move"><div class="wrap">
  <h2>How hard is it to move your cloud?</h2>
  <div class="carousel">
    <svg class="arrow" viewBox="0 0 44 96"><polygon points="44,0 44,96 0,48" fill="#0c1459"/></svg>
    <div class="cards">
      <div class="card"><div class="name"><i></i>Northvault</div><a class="btn btn-navy">View More</a></div>
      <div class="card"><div class="name"><i></i>Skyreach</div><a class="btn btn-navy">View More</a></div>
      <div class="card"><div class="name"><i></i>Orbitly</div><a class="btn btn-navy">View More</a></div>
    </div>
    <svg class="arrow" viewBox="0 0 44 96"><polygon points="0,0 0,96 44,48" fill="#0c1459"/></svg>
  </div>
</div></section>

<section class="advice">
  <h2>Knowledgeable independent advice matters</h2>
  <p>Traditionally, the balance of power lies with &nbsp;your host, who has no interest in your moving to another platform. It may also be that your cloud supplier is a linked to your IT firm, developer or even staff preferences - and in some cases they will specialise in only one of these suppliers.</p>
  <p>It’s time to break free . VRN equips companies, resellers and consultants with the power to choose, to negotiate, to move. We can do this for you.</p>
</section>

<section class="costs">
  <h2>Make your cloud costs evaporate</h2>
  <div class="badge"><b>20%</b><span>CHEAER</span></div>
  <div class="copy">
    <p>As cloud costs continue to escalate , and as you suddenly hit new tiers of spend, you may feel helpless in the face of rising costs.</p>
    <p>However, even taking the cost of moving into acount, VRN has estimated the average client will save 20% of spend on their cloud by using us to find the best solution and help you to move there.</p>
    <a class="btn">See Case Study</a>
  </div>
</section>

<section class="start">
  <h2>Let’s get started</h2>
  <p>If you would like to speak to a friendly and helpful member of our team, ask questions, disuss option or to help with anything on your mind, please get in touch</p>
  <div class="row"><a class="btn btn-red">Call &nbsp;01632 960 418</a><a class="btn btn-red">Send an Email</a></div>
</section>

<section class="blog">
  <h2>VRN Blog</h2>
  <div class="posts">
    <article class="post"><div class="thumb" role="img" aria-label="Flat illustration of people working with cloud dashboards"></div><h3>News headline or blog story</h3></article>
    <article class="post"><div class="thumb" role="img" aria-label="Flat illustration of people working with cloud dashboards"></div><h3>News headline or blog story</h3></article>
    <article class="post"><div class="thumb" role="img" aria-label="Flat illustration of people working with cloud dashboards"></div><h3>News headline or blog story</h3></article>
    <article class="post"><div class="thumb" role="img" aria-label="Flat illustration of people working with cloud dashboards"></div><h3>News headline or blog story</h3></article>
  </div>
</section>

<section class="trusted">
  <h2>Trusted by</h2>
  <div class="logos">
    <div class="logo-box">Kenzora</div>
    <div class="logo-box"><div class="mark"></div></div>
    <div class="logo-box">Clearsight</div>
    <div class="logo-box">Pedalo</div>
  </div>
</section>

<footer class="footer">
  <div class="col"><h4>Trusted by</h4><ul><li>Northvault</li><li>Skyreach</li><li>Orbitly</li><li>Ironbyte</li><li>Sagebase</li><li>Tidecloud</li><li>Others</li><li>Private Cloud</li></ul></div>
  <div class="col"><h4>Services</h4><ul><li>Cloud Cost Review</li><li>Migration Planing</li><li>MigrationExecution</li><li>Security &amp; Compliance</li><li>SOFTWARE</li><li>Skygate</li><li>ArcShift</li></ul></div>
  <div class="col"><h4>About VRN</h4><ul><li>Blogs</li><li>Partners</li><li>About Us</li><li>Contact Us</li></ul></div>
  <div class="col"><h4>Contact</h4><ul><li>[T] 01632 960 418</li><li>[E] Email Us</li><li>[L] ProNet</li></ul>
    <address>Harrow House<br>Mill Lane<br>Eastwick<br>EW4 2QT<br>England</address></div>
</footer>
</body>
</html>
```